Business Card Design
Brightvale Marks
Modern
Kemi Varo
47 Olumide Bankole Crescent
Wuse 2
Abuja
Nigeria
info@brightvalemarks.com
www.brightvalemarks.com

```html
<!DOCTYPE html>
<html lang="en">
<head>
<meta charset="utf-8">
<title>Brightvale Marks — Business Card</title>
<link rel="stylesheet" href="https://fonts.googleapis.com/css2?family=Tinos:wght@400;700&display=swap">
<style>
  :root {
    --page-bg: #e9e6e1;
    --card-white: #ffffff;
    --brand-blue: #1f86c4;
    --blue-light: #3aa2dd;
    --blue-deep: #1670ad;
    --accent-green: #8cc63f;
    --text-on-blue: #ffffff;
    --shadow: rgba(40, 30, 20, 0.18);
  }
  * { box-sizing: border-box; margin: 0; padding: 0; }
  html, body {
    width: 1200px; height: 871px; overflow: hidden;
    background: var(--page-bg);
    font-family: "Tinos", "Times New Roman", serif;
  }
  .canvas {
    width: 1200px; height: 871px;
    display: flex; flex-direction: column;
    align-items: center; justify-content: center; gap: 40px;
  }
  .card {
    width: 680px; height: 389px;
    background: var(--card-white);
    box-shadow: 0 6px 18px var(--shadow);
    position: relative; overflow: hidden;
  }
  /* front */
  .card-front { display: flex; align-items: center; justify-content: center; }
  .brand-lockup { display: flex; align-items: center; gap: 14px; }
  .brand-dot {
    width: 34px; height: 34px; border-radius: 50%;
    background: var(--accent-green);
  }
  .brand-name {
    color: var(--brand-blue);
    font-weight: 400; font-size: 34px;
    text-transform: uppercase; letter-spacing: 0.5px;
  }
  /* back */
  .card-back { display: flex; }
  .back-brand {
    width: 318px; display: flex; align-items: center; justify-content: center;
  }
  .back-brand .brand-name { font-size: 26px; }
  .back-brand .brand-dot { width: 26px; height: 26px; }
  .accent-stripe { width: 14px; background: var(--accent-green); }
  .stripe-gap { width: 6px; background: var(--card-white); }
  .contact-panel {
    flex: 1; position: relative; color: var(--text-on-blue);
    background: radial-gradient(ellipse at 40% 45%, var(--blue-light) 0%, var(--brand-blue) 55%, var(--blue-deep) 100%);
  }
  .person-name {
    position: absolute; top: 34px; right: 40px;
    font-weight: 700; font-size: 20px;
  }
  .address {
    position: absolute; top: 136px; right: 40px;
    text-align: right; font-size: 18px; line-height: 1.25;
  }
  .contact-list {
    position: absolute; left: 24px; right: 30px; bottom: 26px;
    list-style: none; font-size: 15px; line-height: 1.3;
  }
  .contact-list li { display: flex; align-items: center; gap: 6px; }
  .contact-list .phone { justify-content: flex-end; }
  .contact-list svg { width: 13px; height: 13px; fill: var(--text-on-blue); }
</style>
</head>
<body>
<main class="canvas">
  <section class="card card-front" aria-label="Business card front">
    <div class="brand-lockup">
      <span class="brand-dot"></span>
      <span class="brand-name">Brightvale Marks</span>
    </div>
  </section>

  <section class="card card-back" aria-label="Business card back">
    <div class="back-brand">
      <div class="brand-lockup">
        <span class="brand-dot"></span>
        <span class="brand-name">Brightvale Marks</span>
      </div>
    </div>
    <div class="accent-stripe"></div>
    <div class="stripe-gap"></div>
    <div class="contact-panel">
      <p class="person-name">Kemi Varo</p>
      <address class="address">
        47 Olumide Bankole Crescent<br>
        Wuse 2 Abuja Nigeria
      </address>
      <ul class="contact-list">
        <li>info@brightvalemarks.com</li>
        <li class="phone">08130004721
          <svg viewBox="0 0 24 24" aria-hidden="true"><path d="M6.6 10.8a15 15 0 0 0 6.6 6.6l2.2-2.2c.3-.3.7-.4 1-.2 1.1.4 2.3.6 3.6.6.6 0 1 .4 1 1V20c0 .6-.4 1-1 1A17 17 0 0 1 3 4c0-.6.4-1 1-1h3.5c.6 0 1 .4 1 1 0 1.3.2 2.5.6 3.6.1.3 0 .7-.2 1z"/></svg>
        </li>
        <li>www.brightvalemarks.com</li>
      </ul>
    </div>
  </section>
</main>
</body>
</html>
```